BRIM Outreach Partners Business Card Rebrand

Hello Designers! We are looking for help designing our new business card to go in conjunction with our company rebrand. Unfortunately, we have an event mid June that requires we get these printed ASAP (before our new website is launched.) We have a mostly complete Brand Book which I have uploaded to this request for your reference to company information, style, fonts. I've also enclosed our logo file in .eps & .jpg. Attached is a sample business card my boss liked but said was "too simple." I made it in Canva and do not profess to be a designer. NOT FOR DESIGN REFERENCE, ONLY FOR CONTEXT Here is what our old website looks like: https://brimoutreachpartners.com/.

```html
<!DOCTYPE html>
<html lang="en">
<head>
<meta charset="utf-8">
<title>BRIM Outreach Partners — Business Card</title>
<link rel="stylesheet" href="https://fonts.googleapis.com/css2?family=Roboto+Condensed:wght@300;400;700&display=swap">
<style>
  :root {
    --stage: #232323;
    --card-dark: #1f1f23;
    --brand-blue: #4db3e8;
    --brand-blue-deep: #0a9fe0;
    --ink-white: #ffffff;
    --ink-soft: #e6e6e6;
  }
  * { box-sizing: border-box; margin: 0; padding: 0; }
  html, body {
    width: 1200px; height: 780px; overflow: hidden;
    background: var(--stage);
    font-family: "Roboto Condensed", "Arial Narrow", sans-serif;
  }
  .stage {
    width: 1200px; height: 780px;
    display: flex; align-items: center; justify-content: center; gap: 40px;
  }
  .card {
    position: relative; width: 520px; height: 297px; overflow: hidden;
    box-shadow: 0 18px 40px rgba(0,0,0,.45);
  }
  .card--front { background: var(--card-dark); }
  .card--back { background: var(--brand-blue); display: flex; align-items: center; justify-content: center; }

  .front-curve { position: absolute; inset: 0; }

  .wordmark { display: flex; align-items: center; gap: 10px; }
  .wordmark__dot { width: 30px; height: 30px; border-radius: 50%; background: var(--brand-blue); flex: none; }
  .wordmark__name { font-weight: 700; font-size: 22px; line-height: 1.05; color: var(--ink-white); letter-spacing: .5px; }
  .card--front .wordmark { position: absolute; top: 40px; left: 300px; width: 200px; }
  .card--back .wordmark__dot { width: 56px; height: 56px; background: var(--brand-blue-deep); }
  .card--back .wordmark__name { color: var(--brand-blue-deep); font-size: 36px; }

  .holder { position: absolute; top: 34px; left: 32px; }
  .holder__name { font-weight: 700; font-size: 28px; color: var(--brand-blue); }
  .holder__title { font-weight: 300; font-size: 12px; letter-spacing: .6px; color: var(--ink-white); margin-top: 2px; }

  .divider { position: absolute; left: 252px; top: 118px; width: 1.5px; height: 66px; background: var(--ink-white); }

  .contacts { position: absolute; left: 270px; top: 122px; list-style: none; }
  .contacts li { display: flex; align-items: center; gap: 8px; font-size: 14px; font-weight: 400; color: var(--ink-soft); line-height: 20px; }
  .contacts svg { width: 13px; height: 13px; flex: none; }

  .location { position: absolute; left: 34px; bottom: 26px; font-size: 15px; color: var(--ink-white); font-weight: 400; }
</style>
</head>
<body>
<main class="stage">
  <section class="card card--front" aria-label="Business card front">
    <svg class="front-curve" viewBox="0 0 520 297" aria-hidden="true">
      <path d="M0,92 C40,250 300,285 520,232 L520,297 L0,297 Z" fill="var(--brand-blue)"/>
      <path d="M22,100 C70,238 310,272 505,226" fill="none" stroke="var(--ink-white)" stroke-width="3" stroke-linecap="round"/>
    </svg>

    <div class="holder">
      <h1 class="holder__name">Marcus Delane-Hart</h1>
      <p class="holder__title">MANAGING PARTNER</p>
    </div>

    <div class="wordmark">
      <span class="wordmark__dot"></span>
      <span class="wordmark__name">BRIM Outreach Partners</span>
    </div>

    <span class="divider"></span>

    <ul class="contacts">
      <li>
        <svg viewBox="0 0 24 24"><path fill="var(--brand-blue)" d="M6.6 10.8a15 15 0 0 0 6.6 6.6l2.2-2.2a1 1 0 0 1 1-.25 11.4 11.4 0 0 0 3.6.6 1 1 0 0 1 1 1V20a1 1 0 0 1-1 1A17 17 0 0 1 3 4a1 1 0 0 1 1-1h3.5a1 1 0 0 1 1 1c0 1.25.2 2.45.6 3.6a1 1 0 0 1-.25 1z"/></svg>
        +1-555-201-7743
      </li>
      <li>
        <svg viewBox="0 0 24 24"><circle cx="12" cy="12" r="9" fill="none" stroke="var(--brand-blue)" stroke-width="2"/><path d="M3 12h18M12 3c3 3 3 15 0 18M12 3c-3 3-3 15 0 18" fill="none" stroke="var(--brand-blue)" stroke-width="1.6"/></svg>
        www.brimoutreachpartners.com
      </li>
      <li>
        <svg viewBox="0 0 24 24"><rect x="3" y="6" width="18" height="12" rx="1.5" fill="none" stroke="var(--brand-blue)" stroke-width="2"/><path d="M3 7l9 6 9-6" fill="none" stroke="var(--brand-blue)" stroke-width="2"/></svg>
        marcus@brimoutreachpartners.com
      </li>
    </ul>

    <p class="location">Ashvale, CO based (Mountain Time)</p>
  </section>

  <section class="card card--back" aria-label="Business card back">
    <div class="wordmark">
      <span class="wordmark__dot"></span>
      <span class="wordmark__name">BRIM Outreach Partners</span>
    </div>
  </section>
</main>
</body>
</html>
```